Flyer-Design für Abschleppunternehmen
Zielgruppe
Wir sind ein Abschleppunternehmen und sind bestrebt neue Kunden zu gewinnen. Vor allem im Bereich 'Falschparker' suchen wir Firmen/Unternehmen mit Privatparkplätzen, die von fremden Personen zu geparkt werden. Hierzu ist stark darauf hinzuweisen, dass diese Leistung für den Autraggeber völlig kostenlos und ohne Aufwand anzufordern ist.
Aufgabenstellung
Vorschlag DIN Fyler 21x9,8cm . Wir sind ein 24/7 Betrieb. Rufnr. 073845190. Es ist darauf hinzweisen, dass wir ein unternehmen aus der direkten umgebung sind.

```html
<!DOCTYPE html>
<html lang="de">
<head>
<meta charset="utf-8">
<title>Brennwald Abschleppdienst – Flyer</title>
<link rel="stylesheet" href="https://fonts.googleapis.com/css2?family=Montserrat:wght@600;700;800&family=Open+Sans:wght@400;600;700&display=swap">
<style>
  :root {
    --yellow: #f2c30f;
    --dark: #2f2d2b;
    --red: #d21f1b;
    --white: #ffffff;
    --ink: #1c1b1a;
    --stage: #d9d9d9;
  }
  * { box-sizing: border-box; margin: 0; padding: 0; }
  html, body { width: 1200px; height: 800px; overflow: hidden; }
  body {
    background: var(--stage);
    font-family: "Open Sans", sans-serif;
    color: var(--ink);
    position: relative;
  }
  .flyer {
    position: absolute;
    top: 50px;
    width: 330px;
    height: 700px;
    background: var(--yellow);
    overflow: hidden;
    box-shadow: 0 6px 18px rgba(0,0,0,0.18);
  }
  .flyer--front { left: 245px; }
  .flyer--back { left: 625px; }

  /* Front */
  .service-pill {
    position: absolute; top: 22px; right: -20px;
    background: var(--red); color: var(--white);
    font-family: "Montserrat", sans-serif; font-weight: 700;
    font-size: 19px; padding: 7px 40px 7px 24px; border-radius: 20px 0 0 20px;
  }
  .no-parking { position: absolute; top: 68px; right: 26px; width: 88px; height: 88px; }
  .brand {
    position: absolute; top: 118px; left: 20px;
    display: flex; align-items: center; gap: 8px;
    font-family: "Montserrat", sans-serif; font-weight: 800; font-size: 28px; color: var(--ink);
  }
  .brand__mark { width: 18px; height: 18px; background: var(--red); }
  .headline-band {
    position: absolute; top: 190px; left: 0; width: 100%; height: 82px;
    background: var(--dark); padding: 12px 22px;
    font-family: "Montserrat", sans-serif; font-weight: 800; line-height: 1.15;
  }
  .headline-band__question { color: var(--yellow); font-size: 26px; }
  .headline-band__answer { color: var(--white); font-size: 22px; }
  .photo { position: absolute; }
  .photo--front-truck {
    top: 272px; left: 0; width: 100%; height: 220px;
    background: linear-gradient(180deg, #b9c2cf 0%, #8a6a44 45%, #3a3732 100%);
    border-bottom: 10px solid var(--dark);
  }
  .offer {
    position: absolute; top: 512px; left: 22px; right: 18px;
    font-size: 14.5px; line-height: 1.35; font-weight: 400;
  }
  .jubilee {
    position: absolute; top: 588px; left: 30px; width: 82px; height: 82px;
    border-radius: 50%; background: var(--red); color: var(--white);
    font-family: "Montserrat", sans-serif; font-weight: 800; text-align: center;
    display: flex; flex-direction: column; justify-content: center; line-height: 1;
  }
  .jubilee__number { font-size: 32px; }
  .jubilee__label { font-size: 14px; font-weight: 700; }
  .claim {
    position: absolute; top: 585px; left: 150px; width: 170px;
    font-family: "Montserrat", sans-serif; font-weight: 800; font-size: 15px; line-height: 1.25; text-align: center;
  }
  .phone-rule {
    position: absolute; top: 670px; left: 0; right: 0;
    display: flex; align-items: center; gap: 8px; padding-left: 120px;
  }
  .phone-rule::before, .phone-rule::after { content: ""; height: 2px; background: var(--ink); flex: 1; }
  .phone-rule::before { flex: 0 0 10px; }
  .phone-rule__number { font-family: "Montserrat", sans-serif; font-weight: 800; font-size: 15px; white-space: nowrap; }

  /* Back */
  .photo--back-truck {
    top: 0; left: 0; width: 100%; height: 165px;
    background: linear-gradient(180deg, #dfe3e8 0%, #9aa0a6 55%, #5b5f63 100%);
  }
  .more-band {
    position: absolute; top: 150px; left: 0; width: 260px; height: 40px;
    background: var(--dark); color: var(--white);
    clip-path: polygon(0 0, 100% 0, 88% 100%, 0 100%);
    font-family: "Montserrat", sans-serif; font-weight: 700; font-size: 18px;
    padding: 8px 18px;
  }
  .services {
    position: absolute; top: 200px; left: 22px; list-style: none;
    font-size: 15.5px; line-height: 1.6; font-weight: 600;
  }
  .services li::before { content: "• "; }
  .service-badge {
    position: absolute; top: 262px; right: 14px; width: 82px; height: 82px;
    background: var(--red);
  }
  .gallery {
    position: absolute; top: 400px; left: 0; width: 100%; height: 225px;
    background: var(--dark); padding: 6px;
    display: grid; grid-template-columns: 1fr 1fr; grid-template-rows: 1fr 1fr; gap: 6px;
  }
  .gallery__photo--dusk { background: linear-gradient(180deg, #7f9ec4 0%, #7a5a3c 55%, #45474a 100%); }
  .gallery__photo--garage { background: linear-gradient(180deg, #8b8d90 0%, #c9b24a 55%, #6c6e70 100%); }
  .gallery__photo--lot { background: linear-gradient(180deg, #a8b9cc 0%, #c9a032 55%, #5a5b5d 100%); }
  .web-footer {
    position: absolute; top: 625px; left: 0; width: 100%; height: 75px;
    background: var(--dark); color: var(--white);
    font-family: "Open Sans", sans-serif; font-weight: 700; font-size: 17px;
    display: flex; align-items: center; justify-content: center;
  }
</style>
</head>
<body>

<section class="flyer flyer--front">
  <div class="service-pill">24/7 Service</div>
  <svg class="no-parking" viewBox="0 0 88 88" role="img" aria-label="Parkverbot-Schild">
    <circle cx="44" cy="44" r="42" fill="#ffffff"/>
    <circle cx="44" cy="44" r="35" fill="#ffffff" stroke="#d21f1b" stroke-width="7"/>
    <text x="44" y="60" text-anchor="middle" font-family="Montserrat, sans-serif" font-weight="800" font-size="46" fill="#1c1b1a">P</text>
    <line x1="21" y1="67" x2="67" y2="21" stroke="#d21f1b" stroke-width="7"/>
  </svg>
  <div class="brand"><span class="brand__mark"></span>Brennwald</div>

  <div class="headline-band">
    <div class="headline-band__question">Falschparker?</div>
    <div class="headline-band__answer">Wir erledigen für sie!</div>
  </div>

  <div class="photo photo--front-truck" role="img" aria-label="Gelber Abschlepp-LKW vor herbstlichen Bäumen"></div>

  <p class="offer">Lassen sie unberechtigt geparkte fahrzeuge kostenlos abschleppen!<br>Ein Anruf genügt</p>

  <div class="jubilee"><span class="jubilee__number">50</span><span class="jubilee__label">Jahre</span></div>
  <p class="claim">Wir sind ihr Abschleppdienst der Region!</p>
  <div class="phone-rule"><span class="phone-rule__number">Tel. 07461 3387</span></div>
</section>

<section class="flyer flyer--back">
  <div class="photo photo--back-truck" role="img" aria-label="Gelber Plateau-LKW mit geladenem Sportwagen"></div>
  <div class="more-band">Wir können auch mehr!</div>

  <ul class="services">
    <li>PKW Abschlepp-Bergungsdienst</li>
    <li>LKW Abschlepp-Bergungsdienst</li>
    <li>Kranservice</li>
    <li>Fahrzeugtransporte</li>
    <li>Ölspurbesitigung</li>
    <li>Fahrzeugoffnungen</li>
  </ul>

  <svg class="service-badge" viewBox="0 0 82 82" role="img" aria-label="24/7 Service">
    <rect width="82" height="82" fill="#d21f1b"/>
    <path d="M62 26 A27 27 0 1 0 68 44" fill="none" stroke="#ffffff" stroke-width="4"/>
    <path d="M56 20 L66 22 L62 32" fill="none" stroke="#ffffff" stroke-width="4"/>
    <text x="41" y="44" text-anchor="middle" font-family="Montserrat, sans-serif" font-weight="800" font-size="17" fill="#ffffff">24/7</text>
    <text x="41" y="56" text-anchor="middle" font-family="Montserrat, sans-serif" font-weight="700" font-size="8" fill="#ffffff">SERVICE</text>
  </svg>

  <div class="gallery">
    <div class="gallery__photo--lot" role="img" aria-label="Gelbes Pannenfahrzeug auf einem Parkplatz"></div>
    <div class="gallery__photo--dusk" role="img" aria-label="Gelbes Pannenfahrzeug in der Dämmerung"></div>
    <div class="gallery__photo--garage" role="img" aria-label="Gelber Pick-up in einer Tiefgarage"></div>
    <div class="gallery__photo--garage" role="img" aria-label="Pannenfahrzeug im Parkhaus"></div>
  </div>

  <div class="web-footer">www.autohilfe-brennwald.de</div>
</section>

</body>
</html>
```